Building company with a modern and unique product looking for a business card to help us stand out

We currently have a logo but as our business has grown, we feel that our business card is not reflecting our modern and high quality product and help us stand out from the crowd. Our business is mainly in the construction of new homes using a unique method and materials that makes our homes fire proof, vermin and pest resistant and rated to the maximum cyclone category (category 5). We need a business card that helps us stand out as well as communicating professionalism, high quality and trustworthiness. I have attached our current logo with a black and white option, as well as our business card which is double sided. We would like to retain as much of the information that is currently on our business cards, but presented in a more sleek way. We do like our current colour palette ( white, black, yellow and grey) and have been looking primarily at business cards with a black background however we are open to other combinations of colour and layout as long as we stand out. Please feel free to tweak our logo to make it more suitable for a business card, we like the black option that we use but we have had trouble trying to get the white area to match the rest of the logo and blend effectively into a business card. Please do not hesitate to contact us with any questions as we really want this to be successful!

Target Market(s)

Large contracts including government and larger companies

Industry/Entity Type

Business

We will be providing this business card to potential clients including key government ministers and large funding companies, our business card should show that we are professional and reliable.

Requirements
Must have
• It must be easy to read and pleasing to the eye, It must contain as much of the information on the current business card and unless something really stands out, we will most likely pick a design that has all of the information included. It must include our logo of course and have some colour included.
Nice to have
• We are looking for a high end business card and would like to see designs that reflect this. We like the gloss/matte contrast, plastic cards with opaque/coloured areas and unique features not seen on everyday paper business cards. It would be nice to see a few different colour combinations, we are open to new ideas so please feel free to take some artistic licence.
Should not have
• Must not be too busy, difficult to read or be distracting from the information conveyed. Other than this please feel free to add your own touches and make it unique!

```html
<!DOCTYPE html>
<html lang="en">
<head>
<meta charset="utf-8">
<title>Kestrel Building Company – Business Card</title>
<link rel="stylesheet" href="https://fonts.googleapis.com/css2?family=Open+Sans:wght@400;600;700&display=swap">
<style>
  :root {
    --board: #cccccc;
    --card-black: #000000;
    --card-white: #ffffff;
    --gold: #e0b21a;
    --grey-text: #bdbdbd;
    --name-text: #e6e6e6;
  }
  * { box-sizing: border-box; margin: 0; padding: 0; }
  html, body { width: 1200px; height: 1160px; overflow: hidden; }
  body {
    background: var(--board);
    font-family: "Open Sans", Arial, sans-serif;
    position: relative;
  }
  .card {
    position: absolute;
    left: 202px;
    width: 776px;
    height: 438px;
    background: var(--card-black);
    border: 1px solid #333;
    box-shadow: 6px 8px 10px rgba(0,0,0,0.35);
    overflow: hidden;
  }
  .card--front { top: 87px; }
  .card--back { top: 616px; height: 440px; }
  .card__band {
    position: absolute; left: 0; top: 0; right: 0;
    height: 105px;
    background: var(--card-white);
  }
  .card--back .card__band { height: 108px; }
  .brand__mark {
    position: absolute;
    left: 48px; top: 52px;
    width: 44px; height: 44px;
    background: var(--gold);
  }
  .brand__name {
    position: absolute;
    left: 48px; top: 120px;
    color: var(--card-white);
    font-size: 32px;
    font-weight: 600;
    line-height: 1.15;
  }
  .card--back .brand__name { top: 122px; }
  .person {
    position: absolute;
    right: 48px; top: 124px;
    text-align: right;
  }
  .person__name {
    color: var(--name-text);
    font-size: 30px;
    font-weight: 700;
    line-height: 1.1;
  }
  .person__role {
    color: var(--gold);
    font-size: 19px;
    letter-spacing: 1.5px;
    line-height: 1.3;
  }
  .contact {
    position: absolute;
    right: 48px; top: 317px;
    text-align: right;
    color: var(--grey-text);
    font-size: 20px;
    line-height: 24px;
    list-style: none;
  }
  .tagline {
    position: absolute;
    left: 54px; top: 349px;
    color: var(--gold);
    font-size: 20px;
    letter-spacing: 1.5px;
    line-height: 23px;
  }
  .features {
    position: absolute;
    right: 48px; top: 325px;
    text-align: right;
    color: var(--grey-text);
    font-size: 20px;
    line-height: 24px;
    list-style: none;
  }
</style>
</head>
<body>
  <section class="card card--front">
    <div class="card__band"></div>
    <span class="brand__mark"></span>
    <p class="brand__name">Kestrel Building<br>Company</p>
    <div class="person">
      <p class="person__name">Owen Castell</p>
      <p class="person__role">MANAGING DIRECTOR</p>
    </div>
    <ul class="contact">
      <li>0491 570 156</li>
      <li>(02) 55 501 234</li>
      <li>kestrelbuild@example.com</li>
    </ul>
  </section>

  <section class="card card--back">
    <div class="card__band"></div>
    <span class="brand__mark"></span>
    <p class="brand__name">Kestrel Building<br>Company</p>
    <p class="tagline">Specialising in<br>Homes that are</p>
    <ul class="features">
      <li>Fire Proof</li>
      <li>Climate Proof</li>
      <li>Cyclone Rated (Cat. 5)</li>
    </ul>
  </section>
</body>
</html>
```